Software Company Business Card

We are looking for a new design of our business card. The design will also be used in the rest of our branding and marketing materials as we want to keep it all uniform. We sell POS software to fine/luxury jewelers and also offer other business services as well to help the jeweler manage their business and need something more updated, technical and fresh, preferably more on the masculine side. We do not want any designs with gems in them but if possible would like to incorporate the circle and arrow in the logo into the design, but not a requirement if you can't make it work. I would like to see a variety of the mix. The colors need to remain our blue and orange and the logo can not change. The squiggly lines have been used as our corporate identity for over 20 years and its time to update. Our company name is TELK (Summit Counter Operations Platform).

Target Market(s)

High End Jewelers

Industry/Entity Type

Software

Contact Information for Business Card

Requirements
Must have
• Our logo and the colors must remain the same. Blue is #d95d39 and Orange is #0f5682.
Nice to have
• The circle and arrow incorporated but not a requirement.
Should not have
• Anything jewelry or gem related.

```html
<!DOCTYPE html>
<html lang="en">
<head>
<meta charset="utf-8">
<title>TELK Business Card</title>
<link rel="stylesheet" href="https://fonts.googleapis.com/css2?family=Montserrat:wght@400;500;600;800;900&display=swap">
<style>
  :root {
    --brand-blue: #0f5682;
    --brand-orange: #d95d39;
    --stage: #ebebeb;
    --paper: #ffffff;
    --ink: #0f5682;
  }
  * { margin: 0; padding: 0; box-sizing: border-box; }
  html, body { width: 1200px; height: 1200px; overflow: hidden; }
  body {
    font-family: "Montserrat", Arial, sans-serif;
    background: var(--paper);
    position: relative;
  }
  .stage {
    position: absolute; left: 0; top: 0;
    width: 1200px; height: 900px;
    background: var(--stage);
  }
  .card {
    position: absolute;
    width: 600px; height: 343px;
    background: var(--paper);
    box-shadow: 0 6px 18px rgba(0,0,0,0.12);
    overflow: hidden;
  }
  /* contact side */
  .card--contact { left: 300px; top: 80px; }
  .contact__accent {
    position: absolute; left: 0; top: 0;
    width: 150px; height: 6px; background: var(--brand-blue);
  }
  .contact__divider {
    position: absolute; left: 250px; top: 0;
    width: 2px; height: 100%; background: var(--brand-blue);
  }
  .contact__person {
    position: absolute; right: 370px; top: 78px;
    text-align: right; color: var(--ink);
  }
  .contact__name { font-size: 26px; letter-spacing: 1px; font-weight: 400; }
  .contact__name strong { font-weight: 800; }
  .contact__role { font-size: 13px; font-weight: 500; margin-top: 4px; }
  .wordmark {
    display: flex; align-items: center; gap: 8px;
    font-weight: 900; color: var(--brand-blue); line-height: 1;
  }
  .wordmark__dot { border-radius: 50%; background: var(--brand-orange); flex: none; }
  .contact__brand { position: absolute; right: 36px; top: 40px; font-size: 38px; }
  .contact__brand .wordmark__dot { width: 30px; height: 30px; }
  .contact__list {
    position: absolute; left: 237px; top: 130px; list-style: none;
  }
  .contact__item {
    display: flex; align-items: center; gap: 14px;
    height: 36px; color: var(--ink); font-size: 17px; font-weight: 500;
  }
  .contact__icon {
    width: 28px; height: 28px; border-radius: 50%;
    background: var(--brand-blue); display: flex; align-items: center; justify-content: center;
    flex: none;
  }
  /* logo side */
  .card--front { left: 300px; top: 480px; }
  .front__rule {
    position: absolute; left: 0; top: 168px; width: 100%; height: 6px;
    background: var(--brand-orange);
  }
  .front__ring {
    position: absolute; left: 170px; top: 40px; width: 264px; height: 264px;
    border: 6px solid var(--brand-orange); border-radius: 50%; background: var(--paper);
    display: flex; align-items: center; justify-content: center;
  }
  .front__ring .wordmark { font-size: 46px; }
  .front__ring .wordmark__dot { width: 32px; height: 32px; }
  /* signature lockup */
  .lockup {
    position: absolute; left: 0; top: 960px; width: 1200px;
    display: flex; justify-content: center;
  }
  .lockup .wordmark { font-size: 120px; gap: 22px; }
  .lockup .wordmark__dot { width: 104px; height: 104px; }
</style>
</head>
<body>
  <div class="stage">
    <section class="card card--contact">
      <div class="contact__accent"></div>
      <div class="contact__divider"></div>
      <div class="contact__person">
        <div class="contact__name"><strong>DANA</strong> HOLT</div>
        <div class="contact__role">Project Manager</div>
      </div>
      <div class="wordmark contact__brand"><span>TELK</span><span class="wordmark__dot"></span></div>
      <ul class="contact__list">
        <li class="contact__item">
          <span class="contact__icon"><svg width="14" height="14" viewBox="0 0 14 14"><path d="M7 1a4 4 0 0 0-4 4c0 3 4 8 4 8s4-5 4-8a4 4 0 0 0-4-4z" fill="#fff"/><circle cx="7" cy="5" r="1.5" fill="#0f5682"/></svg></span>
          48 Harbor Lane, Westfield
        </li>
        <li class="contact__item">
          <span class="contact__icon"><svg width="14" height="14" viewBox="0 0 14 14"><path d="M3 1.5l2 0 1 3-1.5 1c.7 1.6 1.9 2.8 3.5 3.5l1-1.5 3 1v2c0 .8-.7 1.5-1.5 1.5C5.5 12 2 8.5 1.5 3c0-.8.7-1.5 1.5-1.5z" fill="#fff"/></svg></span>
          +00 5550 1834 2271
        </li>
        <li class="contact__item">
          <span class="contact__icon"><svg width="14" height="14" viewBox="0 0 14 14"><rect x="1.5" y="3" width="11" height="8" fill="#fff"/><path d="M1.5 3l5.5 4.5L12.5 3" fill="none" stroke="#0f5682" stroke-width="1"/></svg></span>
          hello@telkpos.com
        </li>
        <li class="contact__item">
          <span class="contact__icon"><svg width="14" height="14" viewBox="0 0 14 14"><path d="M2 7l10-5-4 10-1.5-3.5z" fill="#fff"/></svg></span>
          www.telkpos.com
        </li>
      </ul>
    </section>

    <section class="card card--front">
      <div class="front__rule"></div>
      <div class="front__ring">
        <div class="wordmark"><span>TELK</span><span class="wordmark__dot"></span></div>
      </div>
    </section>
  </div>

  <div class="lockup">
    <div class="wordmark"><span>TELK</span><span class="wordmark__dot"></span></div>
  </div>
</body>
</html>
```